Peruvian Take-Out Menu needs a take-out menu

We need a new tri-fold 8.5"x11" take out menu for a Peruvian restaurant based in New Rochelle, NY. We have a vast selections of dishes from appetizers, seafood based dishes, desserts, Peruvian ceviches and more. We have attached the following:

Restaurant information
Pictures of our dishes
de la Casa Logo in pdf format
Menu in word format
Old take out menu for reference only! (our dishes have changed)
Updates

Industry/Entity Type

Restaurant

```html
<!DOCTYPE html>
<html lang="en">
<head>
<meta charset="utf-8">
<title>Peruvian Take-Out Menu</title>
<link href="https://fonts.googleapis.com/css2?family=Libre+Baskerville&family=Open+Sans:ital,wght@1,400&display=swap" rel="stylesheet">
<style>
  :root{
    --wood-dark:#3a1f10;
    --wood-mid:#5a3219;
    --wood-light:#7a4a28;
    --leaf:#7cc242;
    --leaf-dark:#1f6b3a;
    --badge-green:#3aa54a;
    --cream:#f6ecc9;
    --badge-brown:#5a3a1c;
    --text-white:#ffffff;
    --text-soft:#f1e9dd;
    --photo-a:#c9a27a;
    --photo-b:#efe2cf;
  }
  *{box-sizing:border-box;margin:0;padding:0}
  html,body{width:1200px;height:848px;overflow:hidden;background:var(--wood-dark)}
  .menu{
    position:relative;width:1200px;height:848px;overflow:hidden;
    background:
      linear-gradient(90deg,rgba(0,0,0,.15),rgba(255,255,255,.04) 30%,rgba(0,0,0,.12) 60%,rgba(255,255,255,.05) 85%,rgba(0,0,0,.15)),
      linear-gradient(180deg,var(--wood-light),var(--wood-mid) 40%,var(--wood-dark) 75%,var(--wood-mid));
    font-family:"Open Sans",Arial,sans-serif;
  }
  .fold{position:absolute;top:0;bottom:0;width:1px;background:rgba(0,0,0,.25)}
  .photo{position:absolute;border-radius:18px;
    background:radial-gradient(ellipse at 50% 45%,var(--photo-b),var(--photo-a) 60%,rgba(201,162,122,0) 100%)}
  .badge{position:absolute;border-radius:26px;background:var(--badge-green);
    border:3px solid var(--leaf-dark);padding:5px}
  .badge-inner{width:100%;height:100%;border-radius:20px;background:var(--cream);
    border:3px solid var(--badge-brown);display:flex;align-items:center;justify-content:center;
    font-family:"Libre Baskerville",Georgia,serif;font-size:17.5px;color:var(--badge-green);letter-spacing:.5px}
  .item{position:absolute;color:var(--text-white)}
  .price{position:absolute;left:0;top:0;font-family:"Libre Baskerville",Georgia,serif;font-size:13px;line-height:18px}
  .name{font-family:"Libre Baskerville",Georgia,serif;font-size:15px;line-height:18px;color:var(--leaf);white-space:nowrap}
  .desc{font-style:italic;font-size:10px;line-height:12px;color:var(--text-soft)}
  .desc.spaced{margin-top:11px}
  .options{display:flex;margin-top:12px;font-size:11.5px;line-height:16px}
  .option{display:flex;align-items:baseline;gap:5px}
  .option .label{color:var(--leaf)}
  .option .cost{font-family:"Libre Baskerville",Georgia,serif;font-size:13px;color:var(--text-white)}
  .option:first-child{width:114px}
  .left{left:14px}.left .name{padding-left:54px}.left .desc{margin-left:71px;width:296px}.left .options{margin-left:69px}
  .mid{left:413px}.mid .name{padding-left:55px}.mid .desc{margin-left:77px;width:288px}.mid .options{margin-left:77px}
  .right{left:818px}.right .name{padding-left:54px}.right .desc{margin-left:71px;width:300px}.right .options{margin-left:70px}
</style>
</head>
<body>
<main class="menu">
  <div class="fold" style="left:397px"></div>
  <div class="fold" style="left:794px"></div>

  <div class="photo" role="img" aria-label="Photo of appetizers: fried shrimp, ceviche, stuffed avocado and empanadas with dipping sauce" style="left:0;top:0;width:392px;height:194px"></div>
  <div class="badge" style="left:88px;top:123px;width:230px;height:66px"><div class="badge-inner">APPETIZERS</div></div>

  <div class="item left" style="top:218px"><span class="price">$12.95</span><div class="name">Chicharron de Calamares</div><div class="desc">crispy fried calamari served with house tartar sauce and salsa criolla</div></div>
  <div class="item left" style="top:261px"><div class="name">Anticucho Caretillero</div><div class="desc spaced">choice chicken or cow’s heart Peruvian style kebabs, served with Cusco corn and grilled potatoes</div>
    <div class="options"><span class="option"><span class="label">Corazon</span><span class="cost">$15.95</span></span><span class="option"><span class="label">Pollo</span><span class="cost">$15.95</span></span></div></div>
  <div class="item left" style="top:346px"><div class="name">Palta Rellena</div><div class="desc spaced">peruvian avocado stuffed with choice of chicken or shrimp, marinated in Peruvian spices</div>
    <div class="options"><span class="option"><span class="label">Camarones</span><span class="cost">$11.95</span></span><span class="option"><span class="label">Pollo</span><span class="cost">$8.95</span></span></div></div>
  <div class="item left" style="top:432px"><span class="price">$5.95</span><div class="name">Tamal Criollo</div><div class="desc" style="margin-top:3px">peruvian chicken tamale, served with salsa criolla</div></div>
  <div class="item left" style="top:475px"><span class="price">$9.95</span><div class="name">Salchipapa</div><div class="desc" style="margin-top:3px">french fries mixed with sliced hot dogs</div></div>
  <div class="item left" style="top:518px"><span class="price">$8.95</span><div class="name">Papa a la Huancaina</div><div class="desc">boiled potatoes, topped with ají amarillo and queso fresco sauce, egg, olives</div></div>
  <div class="item left" style="top:561px"><span class="price">$8.95</span><div class="name">Ocopa Arequipena</div><div class="desc">boiled potatoes, topped with huacatay sauce and queso fresco, egg, olives</div></div>
  <div class="item left" style="top:603px"><span class="price">$3.95</span><div class="name">Empanada Limena</div><div class="desc" style="margin-top:5px">patties stuffed with choice of chicken or beef</div></div>
  <div class="item left" style="top:646px"><div class="name">Causa</div><div class="desc spaced">cold mashed potato infused with key of lime juice, pressed into a cake with choice of chicken or shrimp</div>
    <div class="options"><span class="option"><span class="label">Camarones</span><span class="cost">$9.95</span></span><span class="option"><span class="label">Pollo</span><span class="cost">$7.95</span></span></div></div>
  <div class="item left" style="top:731px"><span class="price">$10.95</span><div class="name">Choritos a la Chalaca</div><div class="desc">steamed mussels topped with diced onions, tomatoes, lime juice and Cusco corn</div></div>
  <div class="item left" style="top:775px"><span class="price">$19.95</span><div class="name">Piqueo de la Casa</div><div class="desc">Dished combined of Chicharron de Calamares, Papa a la Huancaina, Choritos a la Chalaca and Causa</div></div>

  <div class="badge" style="left:489px;top:20px;width:222px;height:68px"><div class="badge-inner">SOUPS</div></div>

  <div class="item mid" style="top:109px"><div class="name">Aguadito Limeno</div><div class="desc spaced">chicken and vegetable soup mixed with rice and cilantro</div>
    <div class="options"><span class="option"><span class="label">Large</span><span class="cost">$9.95</span></span><span class="option"><span class="label">Small</span><span class="cost">$5.95</span></span></div></div>
  <div class="item mid" style="top:194px"><span class="price">$12.95</span><div class="name">Sopa a la Minuta</div><div class="desc">traditional milk and angel’s hair pasta soup, served with beef and eggs</div></div>
  <div class="item mid" style="top:237px"><span class="price">$12.95</span><div class="name">Caldo de Gallina</div><div class="desc" style="margin-top:5px">hen broth with noodles, scallion, potatoes and hard-boiled egg</div></div>
  <div class="item mid" style="top:280px"><span class="price">$15.95</span><div class="name">Chupe de Camarones Arequipeno</div><div class="desc">shrimp soup mixed with rice, green peas, Cusco corn, milk, eggs and Peruvian spices</div></div>
  <div class="item mid" style="top:322px"><span class="price">$18.95</span><div class="name">Parihuela del Puerto</div><div class="desc" style="margin-top:3px">classic Peruvian seafood soup</div></div>

  <div class="photo" role="img" aria-label="Photo of Peruvian dishes: fried seafood, rice, ceviche, layered causa and creamy scallop dish" style="left:394px;top:367px;width:400px;height:155px"></div>
  <div class="badge" style="left:489px;top:514px;width:222px;height:67px"><div class="badge-inner">CEVICHES</div></div>

  <div class="item mid" style="top:603px"><span class="price">$10.95</span><div class="name">Leche de Tigre</div><div class="desc" style="margin-top:4px">ceviche marinade in fresh lime juice</div></div>
  <div class="item mid" style="top:645px"><span class="price">$12.95</span><div class="name">Tiradito en Salsa de Aji Amarillo</div><div class="desc">sashimi style fish in yellow pepper sauce and fresh lime juice, served with Cusco corn and sweet potatoes</div></div>
  <div class="item mid" style="top:688px"><span class="price">$24.95</span><div class="name">Piqueo Chalaco</div><div class="desc">dish combined of Ceviche de Pescado (Fish Ceviche) and Jalea (Fried Seafood)</div></div>
  <div class="item mid" style="top:730px"><div class="name">Ceviche</div><div class="desc">choice of raw fish, mixed seafood, shrimp or shrimp with octopus, marinated in fresh lime juice, served with red onions, Cusco corn and sweet potatoes</div>
    <div class="options" style="margin-top:2px"><span class="option"><span class="label">Pescado</span><span class="cost">$15.95</span></span><span class="option"><span class="label">Camaron</span><span class="cost">$17.95</span></span></div>
    <div class="options" style="margin-top:4px"><span class="option"><span class="label">Mixto</span><span class="cost">$17.95</span></span><span class="option"><span class="label">Camaron con Pulpo</span><span class="cost">$18.95</span></span></div></div>

  <div class="badge" style="left:847px;top:18px;width:314px;height:70px"><div class="badge-inner">TRADITIONAL DISHES</div></div>

  <div class="item right" style="top:110px"><span class="price">$30.95</span><div class="name">Parrillada Mixta</div><div class="desc">dish combined of grilled NY Strip steak, anticuchos (Peruvian style kebabs), pork chops and sausage</div></div>
  <div class="item right" style="top:158px"><span class="price">$20.95</span><div class="name">Churrasco En Salsa De Camarones</div><div class="desc">NY strip steak topped with shrimps on hot yellow pepper sauce, served with rice</div></div>
  <div class="item right" style="top:204px"><span class="price">$20.95</span><div class="name">Seco Norteno</div><div class="desc">slowly cooked lamb stew in aji panka sauce, served with rice and Peruvian canario beans</div></div>
  <div class="item right" style="top:252px"><span class="price">$17.95</span><div class="name">Seco de Pato Piurano</div><div class="desc">slowly cooked duck stew in aji panka sauce, served with rice and hard-boiled yuccas</div></div>
  <div class="item right" style="top:298px"><span class="price">$18.95</span><div class="name">Tallarines Verdes Con Churrasco</div><div class="desc">linguine pasta in Peruvian style pesto sauce served with grilled NY Strip steak</div></div>
  <div class="item right" style="top:345px"><div class="name">Tacu Tacu</div><div class="desc spaced">peruvian canario beans mixed with rice, served with choice of NY Strip steak or wok-seared beef in soy sauce</div>
    <div class="options"><span class="option"><span class="label">Churrasco</span><span class="cost">$18.95</span></span><span class="option"><span class="label">Lomo</span><span class="cost">$15.95</span></span></div></div>
  <div class="item right" style="top:440px"><span class="price">$19.95</span><div class="name">Churrasco a lo Pobre</div><div class="desc">NY Strip steak served with fried eggs, sweet plantains, French fries and rice</div></div>
  <div class="item right" style="top:487px"><div class="name">Saltado</div><div class="desc spaced">choice of wok-seared steak or chicken, mixed with red onions, tomatoes, in soy sauce, served with French fries and rice</div>
    <div class="options"><span class="option"><span class="label">Pollo</span><span class="cost">$13.95</span></span><span class="option"><span class="label">Lomo</span><span class="cost">$15.95</span></span></div></div>
  <div class="item right" style="top:581px"><span class="price">$18.95</span><div class="name">Aeropuerto</div><div class="desc">peruvian style fried rice, mixed with noodles, chicken, beef and shrimp</div></div>
  <div class="item right" style="top:628px"><div class="name">Arroz Chaufa</div><div class="desc spaced">peruvian style fried rice mixed with choice of beef or chicken</div>
    <div class="options" style="margin-top:15px"><span class="option"><span class="label">Carne</span><span class="cost">$14.95</span></span><span class="option"><span class="label">Pollo</span><span class="cost">$12.95</span></span></div></div>
  <div class="item right" style="top:722px"><span class="price">$15.95</span><div class="name">Seco de Carne</div><div class="desc">beef ribs stew in aji panka sauce, served with with rice and Peruvian canario beans</div></div>
  <div class="item right" style="top:769px"><span class="price">$11.95</span><div class="name">Aji de Gallina</div><div class="desc">shredded chicken in a spicy ají amarillo creamy sauce, hard-boiled egg, olives, potatoes and rice</div></div>
</main>
</body>
</html>
```